Harbourlight Dental Centre Kelvale business cards and presentation folder

dental practice needing innovative black business cards for 2 different dentists witrh appointment details written at the back of the card for the patient.
name of dentists: Dr Anjali R Venkatesan B.D.S., M.P.H (Melb)
Dr. Raj Kalpat B.D.S.

Target Market(s)

professioinal, working class

Industry/Entity Type

Dental Clinic

Contact Information for Business Card

Dr. Raj Kalpat B.D.S.

Font styles to use
Sans Serif

Requirements
Must have
• Front side: logo
• dentist name
• phone number: 07- 5918 2243
• back side: appointment details: date, time,
• Address: 117C, 58 Tarrow Street, Kelvale - 4561, Queensland
• Email: admin@harbourlightdentalkelvale.example.au
• Website: www.harbourlightdental.example.au
• preferable logo colors
Nice to have
• classy look more pleasing

```html
<!DOCTYPE html>
<html lang="en">
<head>
<meta charset="utf-8">
<title>Harbourlight Dental Centre Kelvale – Business Cards</title>
<link rel="stylesheet" href="https://fonts.googleapis.com/css2?family=Didact+Gothic&display=swap">
<style>
  :root {
    --sage: #acc990;
    --ink: #000000;
    --text-dark: #111111;
    --backdrop: #ece6db;
    --card-shadow: rgba(0, 0, 0, 0.28);
  }
  * { margin: 0; padding: 0; box-sizing: border-box; }
  html, body {
    width: 1200px;
    height: 720px;
    overflow: hidden;
    background: var(--backdrop);
  }
  .canvas {
    position: relative;
    width: 1200px;
    height: 720px;
    overflow: hidden;
    background: var(--backdrop);
  }
  .stage {
    position: absolute;
    left: 0;
    top: 0;
    width: 1280px;
    height: 768px;
    transform: scale(0.9375);
    transform-origin: 0 0;
    font-family: "Didact Gothic", sans-serif;
  }
  .card {
    position: absolute;
    overflow: hidden;
    box-shadow: 3px 4px 6px var(--card-shadow);
  }
  .card-shapes {
    position: absolute;
    inset: 0;
    width: 100%;
    height: 100%;
  }
  .card-back { left: 42px; top: 27px; width: 683px; height: 411px; background: var(--sage); }
  .card-front { left: 688px; top: 397px; width: 562px; height: 333px; background: var(--ink); }

  .appointment {
    position: absolute;
    left: 68px;
    top: 18px;
    font-size: 21px;
    line-height: 31px;
    color: var(--text-dark);
    letter-spacing: 0.5px;
  }

  .brand-name {
    position: absolute;
    color: var(--sage);
    text-transform: uppercase;
    text-align: center;
    letter-spacing: 1px;
    line-height: 1.15;
  }
  .card-back .brand-name { left: 140px; top: 158px; width: 400px; font-size: 29px; }
  .card-front .brand-name { left: 60px; top: 68px; width: 340px; font-size: 25px; }

  .contact-list {
    position: absolute;
    left: 73px;
    top: 309px;
    list-style: none;
    font-size: 18px;
    color: var(--text-dark);
  }
  .contact-list li {
    display: flex;
    align-items: center;
    height: 30px;
  }
  .contact-icon {
    width: 24px;
    height: 24px;
    margin-right: 13px;
    flex: none;
  }
  .at-icon { font-size: 24px; line-height: 24px; text-align: center; }

  .dentist-name {
    position: absolute;
    left: 77px;
    top: 240px;
    font-size: 29px;
    letter-spacing: 1.5px;
    color: var(--text-dark);
    text-transform: uppercase;
    -webkit-text-stroke: 0.6px var(--text-dark);
  }
  .dentist-phone {
    position: absolute;
    left: 77px;
    top: 283px;
    display: flex;
    align-items: center;
    font-size: 17px;
    letter-spacing: 1.5px;
    color: var(--text-dark);
  }
  .dentist-phone .contact-icon { width: 16px; height: 22px; margin-right: 8px; }
</style>
</head>
<body>
<div class="canvas">
  <div class="stage">

    <section class="card card-back" aria-label="Appointment card, back">
      <svg class="card-shapes" viewBox="0 0 683 411" preserveAspectRatio="none" aria-hidden="true">
        <polygon points="0,83 508,148 683,70 683,328 171,263 0,338" fill="var(--ink)"/>
      </svg>
      <div class="appointment">
        <p>Date:________</p>
        <p>Time:________</p>
      </div>
      <p class="brand-name">Harbourlight Dental<br>Centre Kelvale</p>
      <ul class="contact-list">
        <li>
          <svg class="contact-icon" viewBox="0 0 24 24" aria-hidden="true">
            <path d="M3 11 L12 3 L21 11 M5 9.5 V21 H10 V15 H14 V21 H19 V9.5" fill="none" stroke="var(--text-dark)" stroke-width="1.6" stroke-linejoin="round"/>
          </svg>
          117C, 58 Tarrow Street, Kelvale - 4561, Queensland
        </li>
        <li>
          <span class="contact-icon at-icon" aria-hidden="true">@</span>
          admin@harbourlightdentalkelvale.example.au
        </li>
        <li>
          <svg class="contact-icon" viewBox="0 0 24 24" aria-hidden="true">
            <g fill="none" stroke="var(--text-dark)" stroke-width="1.5">
              <circle cx="12" cy="12" r="10"/>
              <ellipse cx="12" cy="12" rx="4.5" ry="10"/>
              <line x1="2" y1="12" x2="22" y2="12"/>
              <path d="M4 7 H20 M4 17 H20"/>
            </g>
          </svg>
          www.harbourlightdental.example.au
        </li>
      </ul>
    </section>

    <section class="card card-front" aria-label="Business card, front">
      <svg class="card-shapes" viewBox="0 0 562 333" preserveAspectRatio="none" aria-hidden="true">
        <polygon points="0,233 417,151 562,248 562,333 0,333" fill="var(--sage)"/>
      </svg>
      <p class="brand-name">Harbourlight Dental<br>Centre Kelvale</p>
      <p class="dentist-name">Dr. Raj Kalpat B.D.S</p>
      <p class="dentist-phone">
        <svg class="contact-icon" viewBox="0 0 16 22" aria-hidden="true">
          <rect x="1.5" y="1" width="13" height="20" rx="2.5" fill="none" stroke="var(--text-dark)" stroke-width="1.8"/>
          <line x1="6" y1="17.5" x2="10" y2="17.5" stroke="var(--text-dark)" stroke-width="1.6"/>
        </svg>
        07- 5918 2243
      </p>
    </section>

  </div>
</div>
</body>
</html>
```